Stationery - Jewellers
Business Card, Letterhead, Envelope.
I need double sided standard sized Business Card [3.5" x 2"]
Anything that looks good. Including the fonts in logo.
Professional
Imran Kazemi
Proprietor
148 Wexcombe Lane
BX4 7QT
Leeds
United Kingdom
info@corwinthegoldcrafts.co.uk
corwinthegoldcrafts.co.uk
I will welcome any ideas.
Logo and tagline: Professionals in making your loved ones smile..
Website address.
Find us on Facebook/Twitter logos.

```html
<!DOCTYPE html>
<html lang="en">
<head>
<meta charset="utf-8">
<title>Corwin – Stationery Set</title>
<link rel="stylesheet" href="https://fonts.googleapis.com/css2?family=Cormorant+Garamond:wght@500;700&family=Lato:wght@400;700&display=swap">
<style>
:root{
  --backdrop:#5e3420;
  --gold:#c9962e;
  --gold-light:#f2d27a;
  --gold-dark:#8a6114;
  --ink:#1a1a1a;
  --paper:#ffffff;
  --grey:#b9b9bd;
  --grey-light:#e4e4e7;
  --text:#444;
}
*{margin:0;padding:0;box-sizing:border-box}
html,body{width:1200px;height:509px;overflow:hidden}
body{background:var(--backdrop);position:relative;font-family:"Lato",sans-serif;color:var(--text)}
.piece{position:absolute;overflow:hidden;box-shadow:0 2px 6px rgba(0,0,0,.45)}
.brand{font-family:"Cormorant Garamond",serif;font-weight:700;color:var(--gold);line-height:1}
.badge{position:absolute;border-radius:50%;background:var(--ink);border:3px solid var(--gold)}
.small{font-size:5px;line-height:1.5}
.swoosh{position:absolute;left:0;width:100%}
.card{width:197px;height:108px;border-radius:4px}
.card--light{background:var(--paper)}
.card--dark{background:var(--ink);color:#ddd}
.card .holder{position:absolute;right:10px;top:8px;text-align:right;font-size:6px;letter-spacing:.5px;font-weight:700}
.card .holder span{display:block;font-weight:400;font-size:5px;color:var(--gold)}
.card .brand{position:absolute;left:18px;top:30px;font-size:22px}
.card .contact{position:absolute;left:30px;bottom:22px;z-index:2}
.card .web{position:absolute;left:0;right:0;bottom:4px;text-align:center;font-size:5px;color:#222;z-index:2}
.card--dark .web{color:#111}
.card .tagline{position:absolute;left:0;right:0;top:68px;text-align:center;font-family:"Cormorant Garamond",serif;font-size:7px;font-style:normal;color:var(--gold)}
.card .social{position:absolute;right:8px;bottom:5px;display:flex;gap:3px;z-index:2}
.card .social i{width:8px;height:8px;background:#3b5998;border-radius:1px}
.card .social i+i{background:#2aa9e0}
.letterhead{left:444px;top:36px;width:235px;height:420px;background:var(--paper)}
.letterhead .brand{position:absolute;left:20px;top:20px;font-size:24px}
.letterhead .address{position:absolute;right:18px;top:16px;text-align:left;font-size:5px}
.watermark{position:absolute;border-radius:50%;background:radial-gradient(circle,#eeeeF0 40%,#dcdce0 70%,#f4f4f6 72%)}
.envelope-back{background:var(--paper)}
.envelope-front{left:684px;top:288px;width:348px;height:168px;background:var(--paper)}
.envelope-front .brand{position:absolute;left:28px;top:62px;font-size:26px}
.envelope-front .address{position:absolute;left:28px;top:100px}
</style>
</head>
<body>

<!-- Business card: front, light -->
<section class="piece card card--light" style="left:19px;top:132px">
  <div class="holder">IMRAN KAZEMI<span>Proprietor</span></div>
  <div class="brand">Corwin</div>
  <svg class="swoosh" style="bottom:0;height:44px" viewBox="0 0 197 44" preserveAspectRatio="none">
    <defs><linearGradient id="g1" x1="0" x2="1"><stop offset="0" stop-color="#8a6114"/><stop offset=".5" stop-color="#f2d27a"/><stop offset="1" stop-color="#c9962e"/></linearGradient></defs>
    <path d="M0 10 Q90 -4 197 14 V44 H0Z" fill="#b9b9bd"/>
    <path d="M0 16 Q95 4 197 20 V44 H0Z" fill="#fff"/>
    <path d="M0 34 Q100 26 197 30 V44 H0Z" fill="url(#g1)"/>
  </svg>
  <div class="contact small">148 Wexcombe Lane, Leeds BX4 7QT · Tel 0113 496 0721<br>info@corwinthegoldcrafts.co.uk</div>
  <div class="web">corwinthegoldcrafts.co.uk</div>
</section>

<!-- Business card: front, dark -->
<section class="piece card card--dark" style="left:228px;top:132px">
  <div class="holder">IMRAN KAZEMI<span>Proprietor</span></div>
  <div class="brand">Corwin</div>
  <svg class="swoosh" style="bottom:0;height:48px" viewBox="0 0 197 48" preserveAspectRatio="none">
    <defs><linearGradient id="g2" x1="0" x2="1"><stop offset="0" stop-color="#8a6114"/><stop offset=".45" stop-color="#f2d27a"/><stop offset="1" stop-color="#c9962e"/></linearGradient></defs>
    <path d="M0 6 Q90 -4 197 10 V48 H0Z" fill="#c9962e"/>
    <path d="M0 10 Q95 2 197 14 V48 H0Z" fill="url(#g2)"/>
  </svg>
  <div class="contact small" style="color:#222">148 Wexcombe Lane, Leeds BX4 7QT · Tel 0113 496 0721<br>info@corwinthegoldcrafts.co.uk</div>
  <div class="web">corwinthegoldcrafts.co.uk</div>
</section>

<!-- Business card: back, light -->
<section class="piece card card--light" style="left:19px;top:257px">
  <div class="badge" style="left:83px;top:18px;width:32px;height:32px"></div>
  <div class="tagline">~ Professionals in making your loved ones smile.. ~</div>
  <svg class="swoosh" style="bottom:0;height:20px" viewBox="0 0 197 20" preserveAspectRatio="none">
    <path d="M0 8 Q100 0 197 6 V20 H0Z" fill="#e4e4e7"/>
  </svg>
  <div class="web" style="text-align:left;left:10px">corwinthegoldcrafts.co.uk</div>
  <div class="social"><i></i><i></i></div>
</section>

<!-- Business card: back, dark -->
<section class="piece card card--dark" style="left:228px;top:257px">
  <div class="badge" style="left:83px;top:18px;width:32px;height:32px;background:#000"></div>
  <div class="tagline">~ Professionals in making your loved ones smile.. ~</div>
  <div class="web" style="color:#ccc">corwinthegoldcrafts.co.uk</div>
  <div class="social"><i></i><i></i></div>
</section>

<!-- Letterhead -->
<section class="piece letterhead">
  <div class="brand">Corwin</div>
  <div class="address small">148 Wexcombe Lane, Leeds<br>BX4 7QT, United Kingdom<br>Tel 0113 496 0721<br>info@corwinthegoldcrafts.co.uk</div>
  <div class="watermark" style="left:77px;top:150px;width:82px;height:82px"></div>
  <svg class="swoosh" style="bottom:0;height:46px" viewBox="0 0 235 46" preserveAspectRatio="none">
    <defs><linearGradient id="g3" x1="0" x2="1"><stop offset="0" stop-color="#8a6114"/><stop offset=".5" stop-color="#f2d27a"/><stop offset="1" stop-color="#c9962e"/></linearGradient></defs>
    <path d="M0 8 Q120 -6 235 10 V46 H0Z" fill="#b9b9bd"/>
    <path d="M0 14 Q120 2 235 16 V46 H0Z" fill="#fff"/>
    <path d="M0 36 Q120 28 235 32 V46 H0Z" fill="url(#g3)"/>
  </svg>
</section>

<!-- Envelope back, dark flap -->
<section class="piece envelope-back" style="left:696px;top:24px;width:480px;height:192px">
  <svg style="position:absolute;inset:0" width="480" height="192" viewBox="0 0 480 192">
    <path d="M0 0 H480 L270 100 Q240 112 210 100 Z" fill="#1a1a1a"/>
    <path d="M0 192 L215 104 M480 192 L265 104" stroke="#e4e4e7" stroke-width="1"/>
  </svg>
  <div class="badge" style="left:218px;top:12px;width:44px;height:44px"></div>
</section>

<!-- Envelope back, light flap -->
<section class="piece envelope-back" style="left:696px;top:221px;width:480px;height:175px">
  <svg style="position:absolute;inset:0" width="480" height="175" viewBox="0 0 480 175">
    <path d="M0 0 H480 L270 92 Q240 104 210 92 Z" fill="#f4f4f6" stroke="#d6d6da"/>
  </svg>
</section>

<!-- Envelope front, gold flap -->
<section class="piece envelope-front">
  <svg style="position:absolute;left:0;top:0" width="348" height="60" viewBox="0 0 348 60" preserveAspectRatio="none">
    <defs><linearGradient id="g4" x1="0" x2="1"><stop offset="0" stop-color="#8a6114"/><stop offset=".35" stop-color="#f2d27a"/><stop offset=".7" stop-color="#c9962e"/><stop offset="1" stop-color="#f2d27a"/></linearGradient></defs>
    <path d="M0 0 H348 V24 Q174 70 0 24Z" fill="url(#g4)"/>
  </svg>
  <div class="badge" style="left:154px;top:8px;width:40px;height:40px"></div>
  <div class="brand">Corwin</div>
  <div class="address small">148 Wexcombe Lane<br>Leeds, BX4 7QT<br>Tel 0113 496 0721<br>info@corwinthegoldcrafts.co.uk</div>
  <div class="watermark" style="left:262px;top:92px;width:54px;height:54px"></div>
  <svg class="swoosh" style="bottom:0;height:14px" viewBox="0 0 348 14" preserveAspectRatio="none">
    <path d="M0 6 Q174 0 348 6 V14 H0Z" fill="#b9b9bd"/>
  </svg>
</section>

</body>
</html>
```